Vostra new design for business cards we want to change our existing design. Logo must remain the same

Hello we are the company VoSTra and offer various services regarding transportation and disposal. In addition to our main acquisition of van rental, we also offer disposal and express transportation, so we need new business card designs for our business. Our elders have their time and do not like it anymore. We want to change our existing design. Logo must remain the same as well as the color blue, whether dark or light Does not play a big role in the best medium blue. Logo must be present on the front side. As well as telephone, email, web and location. Big enough but not too big. Back can be redesigned Logo as well as name VoSTra must be present. Important is the text: Van rental Disposal and clearing express transportation. Without bail in red should be noted somewhere. it should be modern but not too playful. rather serious but no beating company Thank you very much

Target Market(s)

Private customers as well as companies we want to change our existing design. Logo must remain the same as well as the color blue, whether dark or light Does not play a big role in the best medium blue. Logo must be present on the front side. As well as telephone, email, web and location. Big enough but not too big. Back can be redesigned Logo as well as name VoSTra must be present. Important is the text: Van rental Disposal and clearing express transportation. Without bail in red should be noted somewhere. it should be modern but not too playful. rather serious but no beating company Thank you very much

Industry/Entity Type

Car Rental

Contact Information for Business Card

we want to change our existing design. Logo must remain the same as well as the color blue, whether dark or light Does not play a big role in the best medium blue.
Logo must be present on the front side.
As well as telephone, email, web and location. Big enough but not too big.
Back can be redesigned Logo as well as name VoSTra must be present.
Important is the text:
Van rental
Disposal and clearing
Express transportation.
Without bail in red should be noted somewhere.
it should be modern but not too playful. rather serious but no beating company
Thank you very much

Font styles to use
Sans Serif

Colors
33a6d7
ec1f27
0692cd
3277b5

Requirements
Must have
• logo and name VoSTra as described in the above text must have it. we want to change our existing design. Logo must remain the same as well as the color blue, whether dark or light Does not play a big role in the best medium blue. Logo must be present on the front side. As well as telephone, email, web and location. Big enough but not too big. Back can be redesigned Logo as well as name VoSTra must be present. Important is the text: Van rental Disposal and clearing express transportation. Without bail in red should be noted somewhere. it should be modern but not too playful. rather serious but no beating company Thank you very much
Nice to have
• see description we want to change our existing design. Logo must remain the same as well as the color blue, whether dark or light Does not play a big role in the best medium blue. Logo must be present on the front side. As well as telephone, email, web and location. Big enough but not too big. Back can be redesigned Logo as well as name VoSTra must be present. Important is the text: Van rental Disposal and clearing express transportation. Without bail in red should be noted somewhere. it should be modern but not too playful. rather serious but no beating company Thank you very much
Should not have
• Blue White and little red we want to change our existing design. Logo must remain the same as well as the color blue, whether dark or light Does not play a big role in the best medium blue. Logo must be present on the front side. As well as telephone, email, web and location. Big enough but not too big. Back can be redesigned Logo as well as name VoSTra must be present. Important is the text: Van rental Disposal and clearing express transportation. Without bail in red should be noted somewhere. it should be modern but not too playful. rather serious but no beating company Thank you very much

```html
<!DOCTYPE html>
<html lang="en">
<head>
<meta charset="utf-8">
<title>Vostra GmbH – Business Cards</title>
<link href="https://fonts.googleapis.com/css2?family=Rubik:wght@400;500&display=swap" rel="stylesheet">
<style>
  :root {
    --navy: #27286f;
    --navy-deep: #1f2060;
    --steel: #7d9bb8;
    --red: #ec1f27;
    --white: #ffffff;
    --ink: #2a2a4a;
    --stage: #2b2b2d;
  }
  * { box-sizing: border-box; margin: 0; padding: 0; }
  html, body { width: 1200px; height: 930px; overflow: hidden; }
  body {
    background: var(--stage);
    font-family: "Rubik", Arial, sans-serif;
    display: flex;
    flex-direction: column;
    align-items: center;
    justify-content: center;
    gap: 56px;
  }
  .card {
    position: relative;
    width: 620px;
    height: 354px;
    border-radius: 18px;
    overflow: hidden;
  }

  /* Back side */
  .card--back {
    background: var(--navy);
    color: var(--white);
  }
  .card--back .brand {
    position: absolute;
    left: 0; right: 0; top: 120px;
    display: flex;
    justify-content: center;
    align-items: center;
    gap: 16px;
  }
  .brand__mark {
    width: 26px; height: 26px;
    background: currentColor;
  }
  .brand__name {
    font-size: 58px;
    font-weight: 500;
    letter-spacing: 2px;
    line-height: 1;
  }
  .card--back .tagline {
    position: absolute;
    left: 0; right: 0; bottom: 38px;
    text-align: center;
    font-size: 14px;
    letter-spacing: 0.6px;
    text-transform: uppercase;
  }

  /* Front side */
  .card--front {
    background: var(--white);
    color: var(--navy);
  }
  .card--front .brand {
    position: absolute;
    left: 44px; top: 48px;
    display: flex;
    align-items: center;
    gap: 12px;
  }
  .card--front .brand__mark { width: 22px; height: 22px; }
  .card--front .brand__name { font-size: 46px; }
  .holder {
    position: absolute;
    right: 40px; top: 62px;
    text-align: right;
  }
  .holder__name {
    font-size: 25px;
    font-weight: 500;
    text-transform: uppercase;
    letter-spacing: 0.3px;
    line-height: 1.1;
  }
  .holder__role {
    font-size: 15px;
    color: var(--ink);
  }
  .rule {
    position: absolute;
    height: 1.5px;
    background: var(--navy);
  }
  .rule--holder { right: 30px; top: 122px; width: 270px; }
  .rule--contact { left: 40px; top: 220px; width: 290px; }
  .contacts {
    position: absolute;
    left: 44px; top: 232px;
    list-style: none;
    font-size: 16px;
    color: var(--ink);
    line-height: 1.45;
  }
  .contacts li { display: flex; align-items: center; gap: 10px; }
  .contacts svg { width: 12px; height: 12px; flex: none; }
  .contacts .accent { color: var(--red); }
  .address {
    position: absolute;
    right: 40px; top: 226px;
    text-align: right;
    font-size: 16px;
    color: var(--ink);
    line-height: 1.35;
  }
  .footer-band {
    position: absolute;
    left: 0; bottom: 0;
    width: 620px; height: 90px;
  }
</style>
</head>
<body>

  <section class="card card--back" aria-label="Card back">
    <div class="brand">
      <span class="brand__mark"></span>
      <span class="brand__name">VOSTRA</span>
    </div>
    <p class="tagline">Van rental - Disposal and clearing - Express transportation.</p>
  </section>

  <section class="card card--front" aria-label="Card front">
    <div class="brand">
      <span class="brand__mark"></span>
      <span class="brand__name">VOSTRA</span>
    </div>

    <div class="holder">
      <p class="holder__name">Daniel Brooks</p>
      <p class="holder__role">Director</p>
    </div>
    <div class="rule rule--holder"></div>

    <div class="rule rule--contact"></div>
    <ul class="contacts">
      <li>
        <svg viewBox="0 0 12 12" aria-hidden="true"><path d="M2.5 1 L4.5 1 L5 3.5 L3.8 4.4 Q5 7 7.6 8.2 L8.5 7 L11 7.5 L11 9.5 Q10.5 11 9 11 Q1 10 1 2.5 Q1 1 2.5 1Z" fill="var(--navy)"/></svg>
        +330 2460-5172
      </li>
      <li>
        <svg viewBox="0 0 12 12" aria-hidden="true"><rect x="1" y="2.5" width="10" height="7" fill="none" stroke="var(--navy)" stroke-width="1.3"/><path d="M1 2.5 L6 6.5 L11 2.5" fill="none" stroke="var(--navy)" stroke-width="1.3"/></svg>
        info@vostragmbh.com
      </li>
      <li>
        <svg viewBox="0 0 12 12" aria-hidden="true"><circle cx="6" cy="6" r="5" fill="none" stroke="var(--navy)" stroke-width="1.2"/><path d="M1 6 H11 M6 1 Q3 6 6 11 Q9 6 6 1" fill="none" stroke="var(--navy)" stroke-width="1"/></svg>
        <span>www.<span class="accent">vostragmbh</span>.com</span>
      </li>
    </ul>

    <p class="address">48 Harlow St,<br>Benmore VIC 3712</p>

    <svg class="footer-band" viewBox="0 0 620 90" aria-hidden="true">
      <path d="M0 70 L405 70 C432 70 440 40 470 40 L620 40" fill="none" stroke="var(--red)" stroke-width="5"/>
      <path d="M0 80 L415 80 C442 80 450 50 480 50 L620 50 L620 90 L0 90 Z" fill="var(--navy)"/>
    </svg>
  </section>

</body>
</html>
```